Create Lanternfield HR Business Cards.

Create Business Cards for Lanternfield HR. 2 sided and Would like the back to have the logo.

Info for Business Card:
Address: 4827 Millbrook Ave Suite 230 Cleveland, Ohio 44987
Office Number: 216-555-0143
Mobile: 216-555-0192

Website: www.lanternfieldhr.example

Target Market(s)

Small to medium size businesses

Industry/Entity Type

Human Resources

Contact Information for Business Card

Company logo and information

Font styles to use
Serif
Sans Serif

Requirements
Must have
• Info for Business Card: Address: 4827 Millbrook Ave Suite 230 Cleveland, Ohio 44987 Office Number: 216-555-0143 Mobile: 216-555-0192 Website: www.lanternfieldhr.example

```html
<!DOCTYPE html>
<html lang="en">
<head>
<meta charset="utf-8">
<title>Lanternfield HR Business Cards</title>
<link href="https://fonts.googleapis.com/css2?family=Lato:wght@300;400;700;900&display=swap" rel="stylesheet">
<style>
  :root {
    --navy: #241f5e;
    --orange: #f7860f;
    --white: #ffffff;
    --stage: #2b2b2d;
  }
  * { box-sizing: border-box; margin: 0; padding: 0; }
  html, body {
    width: 1200px; height: 900px; overflow: hidden;
    background: var(--stage);
    font-family: "Lato", Arial, sans-serif;
  }
  .stage {
    width: 1200px; height: 900px;
    display: flex; align-items: center; justify-content: center; gap: 80px;
  }
  .card {
    width: 400px; height: 700px;
    background: var(--navy);
    border-radius: 26px;
    box-shadow: 0 4px 0 var(--orange);
    position: relative;
    color: var(--white);
  }
  .brand {
    display: flex; align-items: center; justify-content: center; gap: 12px;
  }
  .brand-dot {
    width: 34px; height: 34px; border-radius: 50%; background: var(--orange);
  }
  .brand-name {
    font-weight: 900; font-size: 30px; color: var(--white); letter-spacing: 0.5px;
  }
  .card-front .brand { position: absolute; top: 90px; left: 0; right: 0; }
  .identity { position: absolute; top: 210px; left: 0; right: 0; text-align: center; }
  .person-name {
    color: var(--orange); font-weight: 900; font-size: 36px;
    text-transform: uppercase; letter-spacing: 0.5px;
  }
  .person-title { font-weight: 300; font-size: 22px; margin-top: 2px; }
  .icon-row {
    position: absolute; top: 318px; left: 0; right: 0;
    display: flex; align-items: center; justify-content: center; gap: 12px;
  }
  .icon-row .dash { width: 40px; height: 2px; background: var(--orange); }
  .icon {
    width: 34px; height: 34px; border-radius: 50%; background: var(--orange);
    display: flex; align-items: center; justify-content: center;
  }
  .contact-lines {
    position: absolute; top: 384px; left: 0; right: 0;
    list-style: none; text-align: center; font-size: 22px; line-height: 1.5;
  }
  .divider {
    position: absolute; top: 550px; left: 40px; right: 40px;
    height: 2px; background: var(--orange);
  }
  .address {
    position: absolute; top: 578px; left: 0; right: 0;
    font-style: normal; text-align: center; font-size: 22px; line-height: 1.45;
  }
  .card-back { display: flex; align-items: center; justify-content: center; }
  .card-back .brand-name { font-size: 34px; }
  .card-back .brand-dot { width: 40px; height: 40px; }
</style>
</head>
<body>
<main class="stage">
  <section class="card card-front" aria-label="Business card front">
    <div class="brand">
      <span class="brand-dot"></span>
      <span class="brand-name">Lanternfield HR</span>
    </div>
    <div class="identity">
      <h1 class="person-name">Daniel Reyes</h1>
      <p class="person-title">Founder &amp; CEO</p>
    </div>
    <div class="icon-row">
      <span class="dash"></span>
      <span class="icon" aria-label="Address">
        <svg width="18" height="18" viewBox="0 0 24 24"><path d="M12 2a7 7 0 0 0-7 7c0 5 7 13 7 13s7-8 7-13a7 7 0 0 0-7-7zm0 9.5A2.5 2.5 0 1 1 12 6.5a2.5 2.5 0 0 1 0 5z" fill="#fff"/></svg>
      </span>
      <span class="icon" aria-label="Office phone">
        <svg width="18" height="18" viewBox="0 0 24 24"><path d="M6.6 10.8a15 15 0 0 0 6.6 6.6l2.2-2.2a1 1 0 0 1 1-.25 11 11 0 0 0 3.6.6 1 1 0 0 1 1 1V20a1 1 0 0 1-1 1A17 17 0 0 1 3 4a1 1 0 0 1 1-1h3.5a1 1 0 0 1 1 1c0 1.25.2 2.45.6 3.6a1 1 0 0 1-.25 1z" fill="#fff"/></svg>
      </span>
      <span class="icon" aria-label="Mobile">
        <svg width="18" height="18" viewBox="0 0 24 24"><rect x="7" y="2" width="10" height="20" rx="2" fill="#fff"/><rect x="9" y="5" width="6" height="11" fill="#f7860f"/></svg>
      </span>
      <span class="icon" aria-label="Email">
        <svg width="18" height="18" viewBox="0 0 24 24"><rect x="3" y="6" width="18" height="12" rx="1" fill="#fff"/><path d="M3 6l9 7 9-7" fill="none" stroke="#f7860f" stroke-width="1.6"/></svg>
      </span>
      <span class="icon" aria-label="Website">
        <svg width="18" height="18" viewBox="0 0 24 24" fill="none" stroke="#fff" stroke-width="1.8"><circle cx="12" cy="12" r="9"/><path d="M3 12h18M12 3c3 3 3 15 0 18M12 3c-3 3-3 15 0 18"/></svg>
      </span>
      <span class="dash"></span>
    </div>
    <ul class="contact-lines">
      <li>216-555-0143</li>
      <li>216-555-0192</li>
      <li>info@lanternfieldhr.example</li>
      <li>lanternfieldhr.example</li>
    </ul>
    <div class="divider"></div>
    <address class="address">4827 Millbrook Ave, Suite 230<br>Cleveland, Ohio 44987</address>
  </section>

  <section class="card card-back" aria-label="Business card back">
    <div class="brand">
      <span class="brand-dot"></span>
      <span class="brand-name">Lanternfield HR</span>
    </div>
  </section>
</main>
</body>
</html>
```